Create a Poster for a True Crime Tour

Kellmore's Old Lantern Walk Poster Design

We need a square and a4 sized poster to promote a true crime tour. The tour covers stories from Brisbane Australia between the 1850s to 1950s.

I would like a vintage style poster design.

Feel free to use the attached images for inspiration or find one of your own choosing - I am interested in seeing your interpretation.

When people think of brisbane the following words come to mind:-
river city
bris vegas
sunshine
tropical
nightlife
blood river
hot weather
summer storms

Sick

Target Market(s)

20-55 Age Group (70% female)

Colors

Designer to choose colors to be used in the design.

Requirements
Must have
• "Kellmore's Old Lantern Walk"
• Our Logo (see uploads section)
Nice to have
• Would love to see some Vintage Designs

```html
<!DOCTYPE html>
<html lang="en">
<head>
<meta charset="utf-8">
<title>Kellmore's Old Lantern Walk – Wanted Poster</title>
<link rel="stylesheet" href="https://fonts.googleapis.com/css2?family=Anton&display=swap">
<style>
  :root {
    --paper: #f1f1f1;
    --paper-edge: #e2e2e2;
    --ink: #4a4a4a;
    --wanted-red: #be2026;
    --photo-light: #c9c9c9;
    --photo-dark: #6e6e6e;
  }
  html, body {
    margin: 0;
    padding: 0;
    width: 849px;
    height: 1200px;
    overflow: hidden;
    background: var(--paper);
  }
  .poster {
    position: relative;
    width: 849px;
    height: 1200px;
    background: radial-gradient(ellipse at 50% 45%, #f7f7f7 0%, var(--paper) 60%, var(--paper-edge) 100%);
    font-family: "Anton", "Impact", sans-serif;
    color: var(--ink);
  }
  .poster-type {
    position: absolute;
    inset: 0;
  }
  .poster-type text {
    font-family: "Anton", "Impact", sans-serif;
  }
  .title-line { fill: var(--ink); }
  .wanted { fill: var(--wanted-red); }
  .rule { fill: var(--ink); }
  .more { fill: var(--ink); }
  .brand-name { fill: var(--ink); }
  .suspect-photo {
    position: absolute;
    left: 251px;
    top: 531px;
    width: 347px;
    height: 459px;
    background: radial-gradient(ellipse at 50% 40%, var(--photo-light) 0%, #a9a9a9 55%, var(--photo-dark) 100%);
  }
</style>
</head>
<body>
<main class="poster">
  <svg class="poster-type" width="849" height="1200" viewBox="0 0 849 1200" aria-label="Kellmore's Old Lantern Walk — Wanted — More">
    <text class="title-line" x="77" y="199" font-size="180" textLength="715" lengthAdjust="spacingAndGlyphs">Kellmore's</text>
    <text class="title-line" x="87" y="312" font-size="124" textLength="703" lengthAdjust="spacingAndGlyphs">Old Lantern Walk</text>

    <rect class="rule" x="46" y="330" width="757" height="5"/>
    <text class="wanted" x="204" y="478" font-size="158" textLength="444" lengthAdjust="spacingAndGlyphs">WANTED</text>
    <rect class="rule" x="46" y="492" width="757" height="12"/>

    <text class="more" x="139" y="1156" font-size="136" textLength="272" lengthAdjust="spacingAndGlyphs">MORE</text>

    <circle class="brand-name" cx="492" cy="1092" r="14"/>
    <text class="brand-name" x="516" y="1112" font-size="56" textLength="216" lengthAdjust="spacingAndGlyphs">NIGHT TALES</text>
  </svg>

  <div class="suspect-photo" role="img" aria-label="Vintage black-and-white mugshot of a man in a suit and tie"></div>
</main>
</body>
</html>
```